Brook Haven Yellow Perch Fish Stock and immune system boosts

We are a non-profit that sets up Aquaponics's systems in cities of 5000 or less in the Midwest. We have created a product that uses our yellow perch carcasses as the base for this broth. Our fish are grown in containment from egg to market size fish. This means it is the safest most sustainable product on the market. We also use veggies grown in the same aquaponics system network. One product has oriental overtones and mixed with antioxidants as a gut immune system bacteria booster. The other is a standard broth that has multiple uses. We are looking for packaging for both our broths. We have included our logo (a sketch hive creation). This product packaging will also be a media piece promoting The Brook Haven way of life and a way to raise revenue for the non-profit. We have not chosen the names of products but will be under the "Brook Haven" verbiage. Example is " "Brook Haven Minnow Might stock"
I have added some current examples of packaging

Target Market(s)

consumers and commercial clients

Industry/Entity Type

Grocery Store

Colors

Designer to choose colors to be used in the design.

Requirements
Must have
• Fresh feeling, restorative qualities, safe, sustainable
• Package size is 32 oz. shape is flexible

```html
<!DOCTYPE html>
<html lang="en">
<head>
<meta charset="utf-8">
<title>Brook Haven Minnow MightStock – Carton Panels</title>
<link rel="stylesheet" href="https://fonts.googleapis.com/css2?family=Marcellus+SC&family=Encode+Sans+Condensed:wght@300;400&family=Roboto+Condensed:wght@700&family=Montserrat:wght@600&display=swap">
<style>
  :root {
    --backdrop: #ededed;
    --pattern-white: #f4f4f2;
    --pattern-blue: #2a7f9e;
    --pattern-teal: #1f5f6e;
    --pattern-orange: #ef9a3a;
    --label-orange: #e5860f;
    --label-orange-deep: #d9780a;
    --label-orange-soft: #f0a040;
    --ink-light: #fdf3e3;
    --panel-edge: #d8d8d8;
  }
  * { box-sizing: border-box; margin: 0; padding: 0; }
  html, body {
    width: 978px; height: 1200px; overflow: hidden;
    background: var(--backdrop);
  }
  .carton {
    position: absolute; left: 60px; top: 100px;
    width: 858px; height: 1000px;
    display: flex;
    box-shadow: 0 10px 30px rgba(0,0,0,0.08);
  }
  .panel {
    position: relative; height: 100%;
    overflow: hidden;
  }
  .panel--side { width: 270px; border-right: 1px solid var(--panel-edge); }
  .panel--front { width: 588px; }

  .fish-pattern {
    position: absolute; inset: 0;
    background:
      radial-gradient(circle at 20% 15%, rgba(42,127,158,0.35), transparent 40%),
      radial-gradient(circle at 80% 40%, rgba(239,154,58,0.35), transparent 40%),
      radial-gradient(circle at 30% 75%, rgba(31,95,110,0.35), transparent 40%),
      radial-gradient(circle at 75% 90%, rgba(239,154,58,0.3), transparent 40%),
      var(--pattern-white);
  }

  .label {
    position: absolute;
    background: linear-gradient(180deg, var(--label-orange) 0%, var(--label-orange-deep) 100%);
    color: var(--ink-light);
    text-align: center;
  }
  .panel--side .label { left: 24px; right: 24px; top: 96px; bottom: 110px; padding: 50px 18px 0; }
  .panel--front .label { left: 60px; right: 56px; top: 92px; bottom: 70px; }

  .divider { display: block; margin: 0 auto; }
  .product-name {
    font-family: "Marcellus SC", serif;
    font-weight: 400;
    line-height: 1.05;
    letter-spacing: 0.5px;
  }
  .panel--side .product-name { font-size: 30px; margin: 10px 0 8px; }

  .side-copy {
    font-family: "Encode Sans Condensed", sans-serif;
    font-weight: 300;
    font-size: 13.5px; line-height: 1.55;
    margin-top: 40px;
  }
  .side-copy p { margin-bottom: 18px; }
  .side-copy .copy-head { display: block; font-weight: 400; }

  .brand-mark {
    position: absolute; left: 50%; top: -64px;
    width: 118px; height: 118px; margin-left: -59px;
    border-radius: 50%;
    background: var(--label-orange);
  }
  .brand {
    position: absolute; left: 0; right: 0; top: 82px;
    font-family: "Marcellus SC", serif;
  }
  .brand-name { font-size: 25px; letter-spacing: 0.5px; }
  .brand-region { font-size: 12.5px; letter-spacing: 0.3px; margin-top: 2px; }

  .title-block { position: absolute; left: 0; right: 0; top: 180px; }
  .panel--front .product-name { font-size: 58px; margin: 10px 0; }

  .seal { position: absolute; left: 50%; top: 395px; margin-left: -165px; }

  .natural-badge {
    position: absolute; left: 50%; top: 690px;
    width: 48px; height: 48px; margin-left: -24px;
    border-radius: 50%;
    background: var(--pattern-teal);
    border: 2px solid var(--ink-light);
  }
  .strength {
    position: absolute; left: 0; right: 0; bottom: 40px;
    font-family: "Roboto Condensed", sans-serif;
    font-weight: 700; font-size: 17px; letter-spacing: 0.2px;
    line-height: 20px;
  }
</style>
</head>
<body>
<main class="carton">

  <section class="panel panel--side">
    <div class="fish-pattern" role="img" aria-label="Repeating pattern of small blue, teal and orange fish on white"></div>
    <div class="label">
      <svg class="divider" width="170" height="14" viewBox="0 0 170 14"><line x1="0" y1="7" x2="170" y2="7" stroke="#fdf3e3" stroke-width="1"/><circle cx="85" cy="7" r="3" fill="#fdf3e3"/></svg>
      <h2 class="product-name">Minnow<br>MightStock</h2>
      <svg class="divider" width="170" height="14" viewBox="0 0 170 14"><line x1="0" y1="7" x2="170" y2="7" stroke="#fdf3e3" stroke-width="1"/><circle cx="85" cy="7" r="3" fill="#fdf3e3"/></svg>
      <div class="side-copy">
        <p><span class="copy-head">THIS IS DUMMY TEXT</span>We are a non-profit that sets up Aquaponics's systems in cities of 5000 or less in the Midwest. We have created a product that uses our yellow perch carcasses as the base for this broth. Our fish are grown in containment from egg to market size fish.</p>
        <p><span class="copy-head">THIS IS DUMMY TEXT</span>This means it is the safest most sustainable product on the market. We also use veggies grown in the same aquaponics system network. One product has oriental overtones and mixed with antioxidants as a gut immune system bacteria booster.</p>
        <p><span class="copy-head">THIS IS DUMMY TEXT</span>This product packaging will also be a media piece promoting The Brook Haven way of life and a way to raise revenue for the non-profit. We have not chosen the names of products but will be under the "Brook Haven" verbiage. Example is "Brook Haven Minnow Might stock"</p>
      </div>
    </div>
  </section>

  <section class="panel panel--front">
    <div class="fish-pattern" role="img" aria-label="Repeating pattern of small blue, teal and orange fish on white"></div>
    <div class="label">
      <div class="brand-mark"></div>
      <div class="brand">
        <div class="brand-name">BROOK HAVEN</div>
        <div class="brand-region">GREAT LAKES REGION</div>
      </div>
      <div class="title-block">
        <svg class="divider" width="200" height="14" viewBox="0 0 200 14"><line x1="0" y1="7" x2="200" y2="7" stroke="#fdf3e3" stroke-width="1.2"/><circle cx="100" cy="7" r="3.5" fill="#fdf3e3"/></svg>
        <h1 class="product-name">Minnow<br>MightStock</h1>
        <svg class="divider" width="320" height="14" viewBox="0 0 320 14"><line x1="0" y1="7" x2="320" y2="7" stroke="#fdf3e3" stroke-width="1.2"/><circle cx="160" cy="7" r="3.5" fill="#fdf3e3"/></svg>
      </div>
      <svg class="seal" width="330" height="280" viewBox="0 0 330 280">
        <defs>
          <path id="arc-top" d="M 45 150 A 120 120 0 0 1 285 150"/>
          <path id="arc-bottom" d="M 30 130 A 135 135 0 0 0 300 130"/>
        </defs>
        <text font-family="Montserrat, sans-serif" font-weight="600" font-size="15" letter-spacing="2" fill="#fdf3e3">
          <textPath href="#arc-top" startOffset="50%" text-anchor="middle">RICH IN ANTIOXIDANTS</textPath>
        </text>
        <rect x="60" y="80" width="210" height="150" rx="60" fill="#f0a040" opacity="0.55" role="img" aria-label="Line drawing of a yellow perch"/>
        <text font-family="Montserrat, sans-serif" font-weight="600" font-size="15" letter-spacing="2" fill="#fdf3e3">
          <textPath href="#arc-bottom" startOffset="50%" text-anchor="middle">AND GUT FRIENDLY PROBIOTICS</textPath>
        </text>
      </svg>
      <div class="natural-badge"></div>
      <div class="strength">CONCENTERATED</div>
    </div>
  </section>

</main>
</body>
</html>
```